Homepage design for Dutch Job Posting Site (Vakmeld.nl)

We need a redesign of our homepage www.Vakmeld.nl to make it very clear what we do. We are an online job posting portal and are looking to recruit clients and professionals on a single page.

The Homepage will focus on CLIENTS (OPDRACHTGEVERS), with the idea that if we have a lot of jobs posted, then the professionals will come.

Important to know is that we now have ONE REGISTRATION for both professionals and clients - so there is no need for two separate registration options.

Also important to know is that the JOB POSTER pages will have a GREEN hyperlinks color (see the color above the OPDRACHTGEVER at the top of the screen) and the Professionals will have a BLUE hyperlinks color (see the color above the PROFESSIONAL at the top of the screen).

At the top of the page, we would like a 4 page slider (we will do the coding but just want 4 slides) that shows how it works and what makes us unique. In the examples below, you can see that we have already done 2 of them, and we will ask the designer to help do the other two once the project is awarded.

You can see from the images provided that we have already done most of the work. The HEADER WRAP and the FOOTER are already done, and you can use these in your examples.

Notice also in the image "Homepage-BannerBlank" the image used in the center. It is an image that is only as wide as the header and then fades off into a background image that we can use repeat-x in the css of the site which fills the screen on any monitor resolution. If you don't understand what I just wrote, you probably are not the right designer for the job.

Notice also that the two images "NU AANMELDEN" and "VAKMELD ESCROW" use background images that have a SUBTLE background image - it is not just a gradient color change. This is what we LOVE in the design so far.

You can see that our design is already very far advanced, so what we are looking for in a new design are not the overall redesign, but specific, subtle design improvements to give the page a CLEAN, FRESH, MODERN look without being busy and crowded.

Where we specifically want help is in these areas. The designers that show us these elements will be the ones selected. All others will be eliminated without further comment:
a) How to blend in the Vakmeld logo into the header design without taking up more HEIGHT (we have done a white overlay, but this is where you can prove to us that you are great.

b) We need a font for our h1 tags in our site. This will be the same font used in "Laatste Opdrachten" "Laatste Blogs" "Zoek uw professional per categorie of rubriek". Do not use a webfont (Arial or Verdana). Instead, refer to the examples provided for inspiration of a font that best suits the site for a header.

c) We need better containers for "Laatse opdrachten", "Laatste Blogs" and Zoek uw professional per categorie of rubriek. They can have colors or just borders or just outlines. They should compliment the site look though and not distract from it.

d) Transitions between the containers and other elements. Right now they are all just boxy and separate, but there could be some overlap, some shadows, an image divider (as there is between "Laatste Blogs" and TornQX) but again, the transitions need top complement the design and not take it over.

Sites that appeal to us for what we are looking for are:
- plumvo.com
- www.ferlindo.com*
- Marblequist.com*
- Tindelvane.com*
*What we like here are both the top PROMINENT central message and then the smaller subtler design transitions underneath.

Feel free to use images or icons to complement the look, but it must be clean, fresh and modern.

Target Market(s)

University-educated Job Posters between 18 - 45

Industry/Entity Type

Online

Requirements
Must have
• - The header wrapper height but be exactly as it is on the images given. This header will be used on all the inner pages and therefore cannot be any higher than what is shown.
- Focus on the 4 tasks outlined
- Keep it clean! We love white, but also like small icons where appropriate and clean transitions.
Nice to have
• Dutch text is NOT important, we can translate.
Should not have
• No cluttered design.

```html
<!DOCTYPE html>
<html lang="nl">
<head>
<meta charset="utf-8">
<title>Vakmeld – Homepage</title>
<link href="https://fonts.googleapis.com/css2?family=Arimo:ital,wght@0,400;0,700;1,400;1,700&display=swap" rel="stylesheet">
<style>
:root{
  --ink:#333;
  --muted:#777;
  --nav:#222;
  --green:#7cc00f;
  --green-dark:#5a9a05;
  --blue:#2f95db;
  --blue-dark:#1f7cc0;
  --panel:#ececec;
  --line:#d6d6d6;
  --sky-top:#9cc6e2;
  --sky-bottom:#5d9dc6;
  --coral-top:#f26b62;
  --coral-bottom:#e2534e;
  --footer:#262626;
}
*{box-sizing:border-box;margin:0;padding:0}
html,body{width:857px;height:1200px;overflow:hidden;background:#fff}
body{position:relative;font-family:"Arimo",Arial,sans-serif;color:var(--ink)}
.abs{position:absolute}

/* header */
.header{left:16px;top:16px;width:825px;height:148px;border-radius:14px 14px 0 0;
  background:linear-gradient(#fdfdfd,#ececec);box-shadow:0 1px 4px rgba(0,0,0,.25)}
.brand{left:36px;top:42px;display:flex;align-items:center;gap:10px}
.brand-mark{width:52px;height:52px;border-radius:50%;background:var(--green)}
.brand-name{font-size:44px;font-weight:700;color:#333;line-height:1;letter-spacing:-1px}
.account{left:659px;top:38px;font-size:11px;color:#222}
.account span{margin:0 9px;color:#555}
.search{left:599px;top:68px;width:213px;height:29px;background:#fff;border:1px solid #ddd;box-shadow:0 1px 3px rgba(0,0,0,.15)}
.search em{position:absolute;left:11px;top:8px;font-size:10px;color:#aaa}
.search b{position:absolute;right:4px;top:3px;width:25px;height:22px;background:linear-gradient(#8fd21c,#5fa308);color:#fff;font-size:10px;text-align:center;line-height:22px}
.nav{left:16px;top:118px;width:825px;height:46px;background:var(--nav);display:flex;align-items:center}
.nav a{color:#fff;text-decoration:none;font-size:12.5px;height:32px;line-height:32px;padding:0 22px;border-right:1px solid #555;position:relative}
.nav a:first-child{padding-left:41px;color:var(--green)}
.nav a:first-child::after{content:"";position:absolute;left:51px;bottom:-7px;border:7px solid transparent;border-bottom-color:#f4f4f4}
.nav a:last-child{border:0}

/* slider */
.slider{left:16px;top:174px;width:825px;height:273px;border:1px solid #ccc;background:#f2f2f2;padding:4px 5px}
.slider-photo{width:100%;height:100%;background:linear-gradient(90deg,#dfe5ea,#9fa8b0 30%,#c9cfd5 55%,#8d959c 80%,#dfe4e8)}
.slide-btn{top:289px;width:42px;height:42px;background:rgba(40,40,40,.75);display:flex;align-items:center;justify-content:center}
.slider-shadow{left:40px;top:447px;width:777px;height:18px;background:radial-gradient(ellipse at top,rgba(0,0,0,.18),transparent 70%)}

/* search panel */
.finder{left:18px;top:486px;width:408px;height:217px;background:var(--panel);border-radius:10px;border:1px solid #e2e2e2}
.finder h1{position:absolute;left:23px;top:20px;font-size:21px;font-weight:700;color:#3d4650}
.finder hr{position:absolute;left:21px;top:51px;width:364px;border:0;border-top:1px solid #bbb}
.radio{top:69px;font-size:17px;color:#777;display:flex;align-items:center;gap:10px}
.radio i{width:10px;height:10px;border:1px solid #777;border-radius:50%;display:inline-block;position:relative}
.radio i.on::after{content:"";position:absolute;left:2px;top:2px;width:4px;height:4px;border-radius:50%;background:var(--green-dark)}
.field{left:20px;width:257px;height:33px;background:#fff;border:1px solid #ddd;font-size:12px;color:#999;padding:9px 13px}
.field .arrow{position:absolute;right:8px;top:9px;width:13px;height:13px;border:1px solid #888;font-size:7px;text-align:center;line-height:12px;color:#333}
.hint{left:285px;top:109px;font-size:8px;color:#666;line-height:11px}
.btn-search{left:303px;top:152px;width:87px;height:29px;border-radius:5px;background:linear-gradient(#a4e32d,#5fae0a);color:#123;font-size:12px;font-weight:700;text-align:center;line-height:29px;box-shadow:0 1px 3px rgba(0,0,0,.3)}

/* post assignment */
.pitch{left:440px;top:505px;width:401px;height:88px;background:var(--panel)}
.pitch p{position:absolute;left:13px;top:15px;font-size:16px;color:#999}
.btn-post{left:273px;top:48px;width:122px;height:28px;background:linear-gradient(#44a9eb,var(--blue-dark));color:#fff;font-size:11.5px;font-weight:700;text-align:center;line-height:28px;box-shadow:0 2px 3px rgba(0,0,0,.25)}
.join{top:612px;width:184px;height:67px;border-radius:4px;background:linear-gradient(#5c5c5c,#2f2f2f);color:#fff;font-size:13px;line-height:19px;padding:13px 0 0 64px;box-shadow:0 2px 3px rgba(0,0,0,.3)}
.join b{display:block}
.join .avatar{position:absolute;left:14px;top:15px;width:36px;height:36px;background:linear-gradient(#777,#444);border:1px solid #888}
.join::after{content:"";position:absolute;left:82px;bottom:-8px;border:8px solid transparent;border-bottom:0;border-top-color:#2f2f2f}

/* latest list */
.latest{left:15px;top:719px;width:514px;height:403px;border:1px solid #c9c9c9;border-radius:5px;background:#fff;box-shadow:0 1px 3px rgba(0,0,0,.12)}
.latest h1{position:absolute;left:11px;top:12px;font-size:16px;font-weight:700;color:#3d4650}
.latest .all{position:absolute;left:355px;top:15px;font-size:12px;font-weight:700;color:#333}
.latest .rule{position:absolute;left:8px;top:40px;width:486px;border-top:1px solid #e3e3e3}
.job{left:11px;width:486px;height:121px;border-bottom:1px solid #e6e6e6}
.job .thumb{position:absolute;left:0;top:1px;width:34px;height:34px;background:#ddd;display:flex;align-items:center;justify-content:center}
.job h2{position:absolute;left:50px;top:0;font-size:13px;font-weight:700;color:#444;text-decoration:underline;text-underline-offset:3px}
.job p{position:absolute;left:50px;top:25px;width:436px;font-size:11px;font-weight:700;color:#555;line-height:15.2px;letter-spacing:-.15px}
.job.active h2,.job.active p{color:var(--blue)}
.job .view{position:absolute;right:0;top:82px;font-size:11px;color:#777}

/* today */
.today{left:548px;top:721px;width:291px;height:115px;background:linear-gradient(var(--sky-top),var(--sky-bottom));color:#fff}
.today h3{position:absolute;left:55px;top:15px;font-size:19px;font-weight:700;font-style:italic}
.today .clock{position:absolute;left:16px;top:13px}
.today p{position:absolute;left:66px;font-size:11px;font-style:italic}
.today p b{font-size:17px;font-weight:400}

/* blogs */
.blogs-head{left:575px;top:858px;width:247px;height:36px;border-radius:0 18px 18px 0;background:linear-gradient(#f2f2f2,#dcdcdc)}
.blogs-head span{position:absolute;left:58px;top:10px;font-size:14px;font-style:italic;color:#444}
.pager{position:absolute;font-size:14px;font-weight:700;letter-spacing:2px}
.blog-icon{left:562px;top:850px;width:46px;height:46px;border-radius:8px;background:linear-gradient(#f7914a,#e0601a)}
.blog-item{left:566px;width:255px;height:19px;background:#eeeeee;font-size:10.5px;color:#444;line-height:19px;padding-left:52px;position:absolute}
.blog-item::before{content:"›";position:absolute;left:38px;color:#777}

/* categories */
.categories{left:548px;top:983px;width:291px;height:138px;background:linear-gradient(var(--coral-top),var(--coral-bottom));color:#fff}
.categories h3{position:absolute;left:8px;top:6px;font-size:17px;font-weight:700;font-style:italic}
.categories .rule{position:absolute;left:8px;top:32px;width:276px;border-top:1px solid rgba(255,255,255,.7)}
.cat-list{position:absolute;top:40px;list-style:none;font-size:9.5px;line-height:15.5px}
.cat-list li::before{content:"›";margin-right:6px}

/* footer */
.footer{left:0;top:1134px;width:857px;height:66px;background:var(--footer);color:#fff;font-size:9.5px}
.footer-links{position:absolute;left:19px;top:17px}
.footer-links span{margin:0 6px;color:#aaa}
.footer .copy{position:absolute;left:19px;top:39px}
.footer .connect{position:absolute;left:590px;top:25px}
.social{position:absolute;top:18px;width:25px;height:25px;border-radius:50%;background:#f1f1f1}
</style>
</head>
<body>

<header>
  <div class="abs header"></div>
  <div class="abs brand"><span class="brand-mark"></span><span class="brand-name">Vakmeld</span></div>
  <div class="abs account">Register<span>|</span>Log in</div>
  <div class="abs search"><em>Search...</em><b>Go</b></div>
  <nav class="abs nav">
    <a href="#">Home</a><a href="#">Assignments</a><a href="#">My Office</a><a href="#">How it works</a><a href="#">Blog</a><a href="#">Contact Us</a>
  </nav>
</header>

<section class="abs slider">
  <div class="slider-photo" role="img" aria-label="Banner photo: a smiling team of five business professionals in an office"></div>
</section>
<div class="abs slide-btn" style="left:48px">
  <svg width="12" height="16" viewBox="0 0 12 16"><path d="M9 2 3 8l6 6" fill="none" stroke="#fff" stroke-width="2.5"/></svg>
</div>
<div class="abs slide-btn" style="left:765px">
  <svg width="12" height="16" viewBox="0 0 12 16"><path d="M3 2l6 6-6 6" fill="none" stroke="#fff" stroke-width="2.5"/></svg>
</div>
<div class="abs slider-shadow"></div>

<section class="abs finder">
  <h1>Zoek</h1>
  <hr>
  <div class="abs radio" style="left:22px"><i class="on"></i>Zoek Professionals</div>
  <div class="abs radio" style="left:211px"><i></i>Zoek Opdrachten</div>
  <div class="abs field" style="top:104px">Vul hier uw zoekopdract in</div>
  <div class="abs hint">De juiste Professional<br>vinden voor uw opdracht</div>
  <div class="abs field" style="top:148px">All Categories<span class="arrow">▼</span></div>
  <div class="abs btn-search">Zoeken</div>
</section>

<section class="abs pitch">
  <p>Wilt u dat professionals vechten om uw opdracht?</p>
  <div class="abs btn-post">Opdracht Plaatsen</div>
</section>
<div class="abs join" style="left:441px"><span class="avatar"></span>Aanmelden als<b>Optrachtgever</b></div>
<div class="abs join" style="left:648px"><span class="avatar"></span>Aanmelden als<b>Professional</b></div>

<section class="abs latest">
  <h1>Laatste Opdrachten</h1>
  <span class="all">Alles Bekijken</span>
  <div class="rule"></div>
  <article class="abs job active" style="top:55px">
    <div class="thumb"><svg width="18" height="18" viewBox="0 0 18 18"><rect x="1" y="1" width="12" height="12" fill="none" stroke="#fff" stroke-width="2"/><rect x="5" y="5" width="12" height="12" fill="none" stroke="#fff" stroke-width="2"/></svg></div>
    <h2>“de Finibus Bonorum et Malorum”</h2>
    <p>Sections 1.10.32 and 1.10.33 from "de Finibus Bonorum et Malorum" by Varonius are also reproduced in their exact original form, accompanied by English versions from the 1914 translation by H. Dellmore.</p>
    <span class="view">Task View</span>
  </article>
  <article class="abs job" style="top:176px">
    <div class="thumb"><svg width="18" height="18" viewBox="0 0 18 18"><rect x="1" y="1" width="12" height="12" fill="none" stroke="#fff" stroke-width="2"/><rect x="5" y="5" width="12" height="12" fill="none" stroke="#fff" stroke-width="2"/></svg></div>
    <h2>“de Finibus Bonorum et Malorum”</h2>
    <p>Sections 1.10.32 and 1.10.33 from "de Finibus Bonorum et Malorum" by Varonius are also reproduced in their exact original form, accompanied by English versions from the 1914 translation by H. Dellmore.</p>
    <span class="view">Task View</span>
  </article>
  <article class="abs job" style="top:297px;border:0">
    <div class="thumb"><svg width="18" height="18" viewBox="0 0 18 18"><rect x="1" y="1" width="12" height="12" fill="none" stroke="#fff" stroke-width="2"/><rect x="5" y="5" width="12" height="12" fill="none" stroke="#fff" stroke-width="2"/></svg></div>
    <h2>“de Finibus Bonorum et Malorum”</h2>
    <p>Sections 1.10.32 and 1.10.33 from "de Finibus Bonorum et Malorum" by Varonius are also reproduced in their exact original form, accompanied by English versions from the 1914 translation by H. Dellmore.</p>
    <span class="view">Task View</span>
  </article>
</section>

<aside>
  <section class="abs today">
    <svg class="clock" width="28" height="28" viewBox="0 0 28 28"><circle cx="14" cy="15" r="11" fill="#fff" stroke="#555" stroke-width="2"/><path d="M14 8v7l5 3" fill="none" stroke="#333" stroke-width="2"/></svg>
    <h3>Vandaag op vakmeld</h3>
    <p style="top:58px">nieuwe opdrachten geplaatst - <b>7</b></p>
    <p style="top:87px">professionals te huur - <b>28</b></p>
  </section>

  <div class="abs blogs-head"><span>Recent Blogs</span><span class="pager" style="left:208px;top:8px;color:#222">‹ ›</span></div>
  <div class="abs blog-icon"></div>
  <div class="blog-item" style="top:912px">Vakmeld Escrow, wat is het eigenlijk?</div>
  <div class="blog-item" style="top:934px">Altijd ondernemer willen zijn</div>
  <div class="blog-item" style="top:956px">Vakmeld van start</div>

  <section class="abs categories">
    <h3>Categories</h3>
    <span class="pager" style="left:258px;top:7px">‹ ›</span>
    <div class="rule"></div>
    <ul class="cat-list" style="left:9px">
      <li>Advies &amp; Educatie</li><li>Design &amp; Multimedia</li><li>Dieren</li><li>Engineering / Manufacturing</li><li>Evenementen en Vrije tijd</li><li>Financiëel &amp; Administratief</li>
    </ul>
    <ul class="cat-list" style="left:147px">
      <li>Gezondheid, Welzijn en Mens</li><li>IT</li><li>Juridisch</li><li>Marketing &amp; Communicatie</li><li>Reparatie en Onderhoud</li><li>Tekst en vertaling</li>
    </ul>
  </section>
</aside>

<footer class="abs footer">
  <div class="footer-links">Home<span>|</span>Assignments<span>|</span>My Office<span>|</span>How it works<span>|</span>Blog<span>|</span>Contact Us<span>|</span>Sitemap</div>
  <div class="copy">Copyright © 2011 www.vakmeld.com All right resereved</div>
  <div class="connect">Connect with us :</div>
  <span class="social" style="left:670px"></span>
  <span class="social" style="left:706px"></span>
  <span class="social" style="left:742px"></span>
  <span class="social" style="left:779px"></span>
  <span class="social" style="left:815px"></span>
</footer>

</body>
</html>
```